Commercial/Corporate Law Firm needs Website Design

Hi guys. I've started up a new law firm and would love your help designing an attractive website. I'll need both design and coding, and to make it easy for us to edit as necessary later, I think it should be built off a Wordpress.org structure.
FIRST IMPRESSIONS
It's very important that the first impression of the website really captures our prospective clients' attention and impresses them. Their first three seconds needs to be good.
I imagine the homepage may be short, with a menu bar and a compelling image, and with a tagline overlaid or underneath (eg. "It's about results.")
The image should be related to our practice areas: eg. IPOs, corporate transactions, or commercial negotiations.
I have previously suggested there could be a skyline image of Sydney or Adelaide. However, because we are based in Adelaide, I don't think Sydney is appropriate - and Adelaide is probably too boring to use.
HOMEPAGE
Being a new firm, we don't have many existing testimonials, and I will be the only lawyer to start with. So we need to focus on the nature of the services we will provide and how my experience can help them. We have an existing logo to use, and I would like the website colour scheme not to clash with that logo (dark blue and white).
After the initial image and tagline there should be a brief introduction to each of the main areas of work, eg. "We specialise in three main areas of practice:"
1. Corporate Transactions and Regulation
2. Business Law and Dispute Resolution
3. Migration Assistance
These should each have an appropriate photo and link to a separate page that briefly describes our services in that area.
Below that there should be a message from me with a photo. Finally, at the bottom, there should be a "Contact Us" section which shows a Google image of our address, contact details, and then our logo with colours inverted.
OTHER PAGES
While we will need some other pages, they should all be fairly simple. I think we will need one page to say "About Us", where I will put information about my experience. I think we will then need one page for each of the 3 areas listed above, which just needs an appropriate image and then text to describe the service. Finally, a "Contact Us" page which I imagine will be the same as the bottom of the homepage.
OTHER DETAILS
For now you can use details from my LinkedIn page to fill out any other text as necessary, or the photo.
Because the logo is square, I would prefer the design of the website also to be rectangular.
Looking forward to seeing your work! Thank you.
Good luck,
Marcus
Target Market(s)
Potential clients:
Businesses with legal issues or disputes
Companies wishing to list on the stock market

```html
<!DOCTYPE html>
<html lang="en">
<head>
<meta charset="utf-8">
<title>Corvell Legal</title>
<link href="https://fonts.googleapis.com/css2?family=Lora:ital,wght@0,400;0,600;1,400&family=Arimo:wght@400;700&display=swap" rel="stylesheet">
<style>
  :root{
    --navy:#0d3b8e;
    --navy-deep:#0a3585;
    --hero-a:#2d5a9c;
    --hero-b:#5a87c2;
    --ink:#333;
    --muted:#666;
    --line:#d6d6d6;
    --paper:#fff;
    --mist:#f4f4f4;
  }
  *{box-sizing:border-box;margin:0;padding:0}
  h1,h2,h3,h4{font-weight:400}
  html,body{width:1200px;height:2500px;overflow:hidden}
  body{position:relative;background:var(--paper);font-family:"Arimo",Arial,sans-serif;color:var(--ink)}
  .abs{position:absolute}

  /* header */
  .site-header{left:0;top:0;width:1200px;height:90px;background:var(--paper);z-index:3}
  .brand-badge{left:85px;top:-8px;width:190px;height:190px;border-radius:50%;background:var(--paper);z-index:4;
    display:flex;flex-direction:column;align-items:center;justify-content:center;gap:12px;padding-top:6px}
  .brand-square{width:50px;height:50px;background:var(--navy)}
  .brand-name{font-family:"Lora",serif;font-weight:400;font-size:19px;letter-spacing:1.5px;color:var(--navy);white-space:nowrap;text-align:center}
  .main-nav{right:87px;top:36px;display:flex;gap:46px;font-family:"Lora",serif;font-size:13px;color:#333;text-transform:uppercase}
  .main-nav .active{color:var(--navy)}

  /* hero */
  .hero{left:0;top:90px;width:1200px;height:565px;background:linear-gradient(110deg,var(--hero-a) 0%,#3b69ad 45%,var(--hero-b) 100%)}
  .hero-kicker{left:0;top:318px;width:1200px;text-align:center;font-family:"Lora",serif;font-size:25px;color:#fff;letter-spacing:1px}
  .hero-title{left:0;top:352px;width:1200px;text-align:center;font-family:"Lora",serif;font-style:italic;font-size:66px;color:#fff}

  /* practice areas */
  .practice-card{left:87px;top:583px;width:1026px;height:459px;background:var(--paper);box-shadow:0 6px 18px rgba(0,0,0,.18)}
  .section-title{font-family:"Lora",serif;font-style:italic;font-size:28px;color:var(--navy);text-align:center}
  .rule{height:3px;width:97px;background:var(--navy)}
  .practice-item{width:308px;height:288px;border:1px solid #e3e3e3;top:712px}
  .practice-photo{width:308px;height:203px}
  .practice-name{height:85px;display:flex;align-items:center;justify-content:center;text-align:center;
    font-family:"Lora",serif;font-style:italic;font-size:19px;line-height:29px;color:var(--navy)}

  /* principal */
  .principal-photo{left:147px;top:1122px;width:536px;height:380px;background:linear-gradient(135deg,#1e2433 0%,#3b3f52 55%,#6a6c7a 100%)}
  .profile-box{left:537px;top:1348px;width:531px;height:299px;background:var(--paper);border:4px solid #dcdcdc;padding:40px 0 0 54px}
  .profile-name{font-family:"Lora",serif;font-style:italic;font-size:30px;color:var(--navy)}
  .profile-role{margin-top:10px;font-family:"Lora",serif;font-size:23px;color:#777;text-transform:uppercase}
  .profile-loc{margin-top:20px;font-size:12px;color:var(--navy)}
  .profile-row{display:flex;margin-top:20px;font-size:12px;color:#555}
  .profile-row .label{width:73px}
  .profile-row .dash{width:30px}

  /* contact */
  .contact{left:0;top:1707px;width:1200px;height:543px;background:var(--mist)}
  .contact-sub{left:0;top:1810px;width:1200px;text-align:center;font-size:12px;color:#666}
  .map{left:87px;top:1862px;width:503px;height:336px;border:2px solid #ddd;background:linear-gradient(140deg,#e9e3c8 0%,#d8dcb8 50%,#c9d6de 100%)}
  .contact-intro{left:638px;top:1888px;width:470px;font-size:12px;line-height:23px;color:#666}
  .contact-head{font-family:"Lora",serif;font-weight:400;font-size:16px;color:#333;text-transform:uppercase}
  .contact-text{font-size:12px;line-height:21px;color:#666}
  .social{top:2140px;left:884px;display:flex;gap:7px}
  .social span{width:37px;height:37px;border-radius:50%;border:2px solid #999}

  /* footer */
  .site-footer{left:0;top:2250px;width:1200px;height:250px;background:var(--navy-deep)}
  .footer-brand{left:0;top:2272px;width:1200px;display:flex;flex-direction:column;align-items:center;gap:16px}
  .footer-brand .brand-square{width:68px;height:68px;background:#fff}
  .footer-brand .brand-name{color:#fff;font-size:32px;letter-spacing:4px}
  .footer-rule{left:92px;top:2428px;width:1016px;height:1px;background:rgba(255,255,255,.18)}
  .copyright{left:0;top:2458px;width:1200px;text-align:center;font-size:12px;color:#fff}
</style>
</head>
<body>

<header class="abs site-header">
  <nav class="abs main-nav">
    <span class="active">Home</span><span>About Us</span><span>Services</span><span>News</span><span>Contact Us</span>
  </nav>
</header>
<div class="abs brand-badge">
  <span class="brand-square"></span>
  <span class="brand-name">CORVELL LEGAL</span>
</div>

<section class="abs hero" role="img" aria-label="City skyline blended with hands working at a laptop, in blue tones"></section>
<p class="abs hero-kicker">CORVELL LAWFIRM</p>
<h1 class="abs hero-title">We Get Results</h1>

<section class="abs practice-card"></section>
<h2 class="abs section-title" style="left:87px;top:620px;width:1026px">We Specialise In Three Main Areas of Practice</h2>
<div class="abs rule" style="left:552px;top:676px"></div>

<article class="abs practice-item" style="left:110px">
  <div class="practice-photo" role="img" aria-label="Hands holding a smartphone over papers" style="background:linear-gradient(135deg,#3a2a24,#8a5a3c 55%,#c79a6a)"></div>
  <div class="practice-name">Corporate Transactions &amp;<br>Regulation</div>
</article>
<article class="abs practice-item" style="left:445px">
  <div class="practice-photo" role="img" aria-label="Business people signing a document" style="background:linear-gradient(135deg,#6d6d6d,#cfcfcf 55%,#2c2c2c)"></div>
  <div class="practice-name">Business Law &amp;<br>Dispute Resolution</div>
</article>
<article class="abs practice-item" style="left:782px">
  <div class="practice-photo" role="img" aria-label="Support agent with headset at a computer" style="background:linear-gradient(135deg,#e6e8ec,#9aa6b8 55%,#4d5a6e)"></div>
  <div class="practice-name">Migration Assistance</div>
</article>

<div class="abs principal-photo" role="img" aria-label="Portrait of the principal in a suit against a night city skyline"></div>
<section class="abs profile-box">
  <h3 class="profile-name">Marcus Corvell</h3>
  <p class="profile-role">Principal at Corvell Legal</p>
  <p class="profile-loc">Adelaide, AustraliaLegal Services</p>
  <div class="profile-row"><span class="label">Current</span><span class="dash">-</span><span>Corvell Legal, Keystone Counsel, Northline Learning</span></div>
  <div class="profile-row"><span class="label">Previous</span><span class="dash">-</span><span>Ashgrove College, Southgate University, Meridian Registry</span></div>
  <div class="profile-row"><span class="label">Education</span><span class="dash">-</span><span>Southgate University</span></div>
</section>

<section class="abs contact"></section>
<h2 class="abs section-title" style="left:0;top:1740px;width:1200px">Contact Us</h2>
<div class="abs rule" style="left:552px;top:1790px"></div>
<p class="abs contact-sub">Sed ut perspiciatis unde omnis iste natus error sit voluptatem accusantium doloremque laudantium</p>
<div class="abs map" role="img" aria-label="Street map showing the office location"></div>
<p class="abs contact-intro">Lorem ipsum dolor sit amet, consectetur adipiscing elit, sed do eiusmod tempor inci did unt ut labore et dolore magna aliqua. Ut enim ad minim veniam, quis nostrud exercitatio ullamco laboris nisi ut aliquip ex ea commodo consequat.</p>

<div class="abs" style="left:638px;top:2002px">
  <h4 class="contact-head">Address</h4>
  <p class="contact-text" style="margin-top:8px"># 2547 Lorem Ipsum Dummy<br>Lorem Ipsum Dummy</p>
</div>
<div class="abs" style="left:890px;top:2002px">
  <h4 class="contact-head">Email Address</h4>
  <p class="contact-text" style="margin-top:8px">General : info@company.com<br>Office :contact@company.com</p>
</div>
<div class="abs" style="left:638px;top:2118px">
  <h4 class="contact-head">Phone</h4>
  <p class="contact-text" style="margin-top:8px">Mobile : (000)-121-1231</p>
</div>
<h4 class="abs contact-head" style="left:890px;top:2102px">Follow Us</h4>
<div class="abs social"><span></span><span></span><span></span><span></span><span></span></div>

<footer class="abs site-footer"></footer>
<div class="abs footer-brand">
  <span class="brand-square"></span>
  <span class="brand-name">CORVELL LEGAL</span>
</div>
<div class="abs footer-rule"></div>
<p class="abs copyright">© Copyright 2018 Law Firm.All Rights Reserved</p>

</body>
</html>
```